Aerial photo/video drone company needs new business card

Aerial visual company who offers photos and video services via drones.

We are QVL certified and work in the real estate, insurance, construction, and film industries.

I'm looking for a clean, professional, maybe even edgy design, that will be a conversation starter when networking.

I've included our logo, current business card, and font.

Our current business card is decent; albeit, I'm looking for something more unique. If you folks provide good designs, I'll definitely guarantee payment (and I'm not opposed to tipping if the design is above and beyond).

Target Market(s)

Insurance companies, real estate agents, construction companies, advertising & other creative agencies, and filmmakers/producers.

Industry/Entity Type

Business

Contact Information for Business Card

Company name pronounced air-a-vee.

Font styles to use
Other font styles liked:
• Font was uploaded; that or similar; not opposed to other fonts if they work well with the design

Requirements
Must have
• Clearly prominent logo; my name and title; phone number; email address; web address; mentioned "QVL Certified" or similar; should indicate "Aerial visual"
Nice to have
• Watermark of logo or otherwise
Should not have
• Pictures of drones or scenic shots

```html
<!DOCTYPE html>
<html lang="en">
<head>
<meta charset="utf-8">
<title>Skyvara business card</title>
<link rel="stylesheet" href="https://fonts.googleapis.com/css2?family=Quicksand:wght@500;600;700&display=swap">
<style>
  :root {
    --navy: #243a5e;
    --sky: #1f8fd8;
    --ink: #2b2f36;
    --paper: #ffffff;
    --backdrop: #7d868c;
  }
  * { box-sizing: border-box; margin: 0; padding: 0; }
  html, body { width: 1200px; height: 900px; overflow: hidden; }
  body {
    background: var(--backdrop);
    font-family: "Quicksand", sans-serif;
    display: flex;
    align-items: center;
    justify-content: center;
    gap: 40px;
  }
  .card {
    position: relative;
    width: 540px;
    height: 309px;
    background: var(--paper);
    overflow: hidden;
  }
  .card__band {
    position: absolute;
    left: 0; right: 0;
    bottom: 20px;
    height: 26px;
    background: var(--navy);
    color: var(--paper);
    font-weight: 600;
    font-size: 13px;
    letter-spacing: 0.2px;
    display: flex;
    align-items: center;
    padding-left: 110px;
  }
  /* front */
  .front__brand {
    position: absolute;
    left: 0; right: 0;
    top: 92px;
    display: flex;
    align-items: center;
    justify-content: center;
    gap: 14px;
    color: var(--navy);
    font-weight: 700;
    font-size: 62px;
    letter-spacing: -1px;
  }
  .brand__mark {
    width: 22px; height: 22px;
    background: var(--sky);
    border-radius: 50%;
  }
  /* back */
  .back__brand {
    position: absolute;
    left: 46px; top: 30px;
    display: flex;
    align-items: center;
    gap: 8px;
    color: var(--navy);
    font-weight: 700;
    font-size: 32px;
    letter-spacing: -0.5px;
  }
  .back__brand .brand__mark { width: 12px; height: 12px; }
  .contact {
    position: absolute;
    left: 46px; top: 100px;
    list-style: none;
    color: var(--ink);
    font-weight: 700;
    font-size: 13px;
  }
  .contact__item {
    display: flex;
    align-items: center;
    gap: 12px;
    height: 26px;
  }
  .contact__icon { width: 13px; height: 13px; fill: var(--navy); flex: none; }
  .holder {
    position: absolute;
    right: 42px; top: 150px;
    text-align: right;
  }
  .holder__name { color: var(--sky); font-weight: 700; font-size: 20px; }
  .holder__title { color: var(--ink); font-weight: 700; font-size: 13px; margin-top: 2px; }
</style>
</head>
<body>
  <section class="card front">
    <div class="front__brand"><span>skyvara</span><span class="brand__mark"></span></div>
    <div class="card__band">QVL Part 107 Commercial sUAS Certified</div>
  </section>

  <section class="card back">
    <div class="back__brand"><span>skyvara</span><span class="brand__mark"></span></div>
    <ul class="contact">
      <li class="contact__item">
        <svg class="contact__icon" viewBox="0 0 16 16"><path d="M4 0h8a1 1 0 0 1 1 1v14a1 1 0 0 1-1 1H4a1 1 0 0 1-1-1V1a1 1 0 0 1 1-1zm1 2v10h6V2zm3 11a1 1 0 1 0 0 2 1 1 0 0 0 0-2z"/></svg>
        555 014 2731
      </li>
      <li class="contact__item">
        <svg class="contact__icon" viewBox="0 0 16 16"><path d="M3.6 1 6 4.2 4.6 6c.9 2 2.6 3.7 4.5 4.6L11 9.2l3.2 2.4-1 2.6c-6.3-.5-11.3-5.5-11.8-11.8z"/></svg>
        555 014 2731
      </li>
      <li class="contact__item">
        <svg class="contact__icon" viewBox="0 0 16 16"><path d="M1 3h14v10H1zm1.5 1.3V5L8 9l5.5-4v-.7L8 8.2z"/></svg>
        dan@skyvara.com
      </li>
      <li class="contact__item">
        <svg class="contact__icon" viewBox="0 0 16 16"><path d="M8 0a8 8 0 1 0 0 16A8 8 0 0 0 8 0zm5.9 7H11a12 12 0 0 0-1.2-5A6 6 0 0 1 13.9 7zM8 2c.8 1 1.5 2.9 1.6 5H6.4C6.5 4.9 7.2 3 8 2zM6.2 2A12 12 0 0 0 5 7H2.1A6 6 0 0 1 6.2 2zM2.1 9H5a12 12 0 0 0 1.2 5A6 6 0 0 1 2.1 9zM8 14c-.8-1-1.5-2.9-1.6-5h3.2C9.5 11.1 8.8 13 8 14zm1.8 0A12 12 0 0 0 11 9h2.9a6 6 0 0 1-4.1 5z"/></svg>
        skyvara.com
      </li>
    </ul>
    <div class="holder">
      <p class="holder__name">Daniel T. Morrow</p>
      <p class="holder__title">Owner, sUAS Pilot</p>
    </div>
    <div class="card__band">Aerial Visual for Real estate-Insurance-Construction-Film</div>
  </section>
</body>
</html>
```